Pristwell Recovery Email Marketing Design

Dear Designer,
We're in need of an email background template for our company, Pristwell Recovery, that reflects our commitment to building lasting relationships with our clients and providing top-quality restoration and cleaning services.
We'd like the template to incorporate our brand colors, which are #F2F2F3, #005EA5, #468ECC, and #000000, and to feature images related to our services, such as water restoration, emergency flood response, mold remediation, trauma scene clean-up, fire restoration, carpet cleaning, and more. Our logo and tagline, "Disaster Undone", should be prominently displayed in a unique and visually appealing way, along with our website address, www.pristwellrecovery.example.
The email should be professional and positive, highlighting the camaraderie and teamwork among our employees. We want to thank our clients for their business, offer a special discount, and promote our services. The final design should be visually stunning and memorable, with a clear call-to-action to encourage clients to take advantage of the discount.
We'd like the final design in JPG or PNG format, with a resolution of at least 720x720 pixels.
Thank you for considering this project. We're excited to see what you come up with!
Best regards,
Dabney
Look and feel
Each slider illustrates characteristics of the customer's brand and the style your logo design should communicate.

```html
<!DOCTYPE html>
<html lang="en">
<head>
<meta charset="utf-8">
<title>Pristwell Recovery – Disaster Undone</title>
<link rel="stylesheet" href="https://fonts.googleapis.com/css2?family=Montserrat:wght@600;700&family=Playfair+Display:wght@700&display=swap">
<style>
  :root {
    --brand-navy: #0a4f9e;
    --brand-blue: #005ea5;
    --brand-sky: #468ecc;
    --band-deep: #3a7cc2;
    --paper: #edf5f9;
    --paper-edge: #dcebf3;
    --text-grey: #9e9fa3;
    --white: #ffffff;
  }
  * { margin: 0; padding: 0; box-sizing: border-box; }
  html, body { width: 1200px; height: 1200px; overflow: hidden; }
  body { background: var(--paper); }
  .card {
    position: relative;
    width: 1200px;
    height: 1200px;
    overflow: hidden;
    background: radial-gradient(circle at 240px 1020px, var(--white) 0%, var(--paper) 45%, var(--paper-edge) 100%);
    font-family: "Montserrat", sans-serif;
  }
  .hero-art { position: absolute; inset: 0; width: 1200px; height: 1200px; }
  .brand {
    position: absolute; left: 60px; top: 58px;
    display: flex; align-items: center; gap: 14px;
    font-family: "Montserrat", sans-serif; font-weight: 700;
    font-size: 30px; color: var(--brand-navy); letter-spacing: 0.5px;
  }
  .brand-dot { width: 18px; height: 18px; border-radius: 50%; background: var(--brand-sky); }
  .headline {
    position: absolute; left: 58px; top: 168px;
    font-family: "Playfair Display", serif; font-weight: 700;
    font-size: 80px; line-height: 88px; color: var(--brand-navy);
  }
  .rule { position: absolute; left: 60px; width: 218px; height: 7px; background: var(--brand-sky); }
  .rule-top { top: 350px; }
  .rule-services { top: 626px; }
  .intro {
    position: absolute; left: 60px; top: 384px; width: 480px;
    font-weight: 700; font-size: 24px; line-height: 29.5px; color: var(--text-grey);
  }
  .services-title {
    position: absolute; left: 60px; top: 558px;
    font-family: "Playfair Display", serif; font-weight: 700;
    font-size: 36px; color: var(--brand-navy);
  }
  .service-list { position: absolute; left: 60px; top: 660px; list-style: none; }
  .service-list li {
    display: flex; align-items: center; height: 64px;
    font-weight: 700; font-size: 23px; color: var(--text-grey);
  }
  .service-list svg { width: 30px; height: 30px; margin-right: 28px; }
  .cta {
    position: absolute; left: 60px; top: 936px; width: 250px; height: 72px;
    border-radius: 36px; background: var(--brand-blue); color: var(--white);
    display: flex; align-items: center; justify-content: center;
    font-weight: 700; font-size: 28px; text-decoration: none;
  }
  .web-band {
    position: absolute; left: 0; top: 1049px; width: 760px; height: 97px;
    background: var(--brand-blue);
    display: flex; align-items: center; padding-left: 58px;
    color: var(--white); font-weight: 700; font-size: 23px;
  }
  .web-band svg { width: 30px; height: 30px; margin-right: 26px; }
</style>
</head>
<body>
<main class="card">
  <div class="brand"><span class="brand-dot"></span>Pristwell Recovery</div>

  <h1 class="headline">DISASTER<br>UNDONE</h1>
  <div class="rule rule-top"></div>

  <p class="intro">Pristwell Recovery, that reflects our commitment to building lasting relationships with our clients and providing top-quality restoration and cleaning services.</p>

  <h2 class="services-title">Our Services</h2>
  <div class="rule rule-services"></div>

  <ul class="service-list">
    <li><svg viewBox="0 0 30 30"><path d="M26 12 A12 12 0 1 1 20 4.5" fill="none" stroke="#4a7fc9" stroke-width="2"/><path d="M9 14 L14 19 L27 5" fill="none" stroke="#4a7fc9" stroke-width="2"/></svg>Water Restoration</li>
    <li><svg viewBox="0 0 30 30"><path d="M26 12 A12 12 0 1 1 20 4.5" fill="none" stroke="#4a7fc9" stroke-width="2"/><path d="M9 14 L14 19 L27 5" fill="none" stroke="#4a7fc9" stroke-width="2"/></svg>Emergency Flood Response</li>
    <li><svg viewBox="0 0 30 30"><path d="M26 12 A12 12 0 1 1 20 4.5" fill="none" stroke="#4a7fc9" stroke-width="2"/><path d="M9 14 L14 19 L27 5" fill="none" stroke="#4a7fc9" stroke-width="2"/></svg>Mold Remediation</li>
    <li><svg viewBox="0 0 30 30"><path d="M26 12 A12 12 0 1 1 20 4.5" fill="none" stroke="#4a7fc9" stroke-width="2"/><path d="M9 14 L14 19 L27 5" fill="none" stroke="#4a7fc9" stroke-width="2"/></svg>Trauma Scene Clean-up</li>
  </ul>

  <a class="cta" href="#">VIEW ALL</a>

  <div class="web-band">
    <svg viewBox="0 0 30 30" fill="none" stroke="#ffffff" stroke-width="2"><circle cx="15" cy="15" r="13"/><ellipse cx="15" cy="15" rx="6" ry="13"/><path d="M2 15 H28 M4 8 H26 M4 22 H26 M15 2 V28"/></svg>
    www.pristwellrecovery.example.
  </div>

  <svg class="hero-art" viewBox="0 0 1200 1200">
    <defs>
      <path id="wave-edge" d="M518,-10 C600,20 690,120 689,213 C688,300 660,400 642,489 C625,580 618,680 618,774 C618,880 640,980 700,1050 C760,1110 860,1150 946,1145 C1040,1140 1130,1100 1200,1059 L1260,1059 L1260,-10 Z"/>
      <linearGradient id="photo-tone" x1="0" y1="0" x2="0.6" y2="1">
        <stop offset="0" stop-color="#ece6df"/>
        <stop offset="0.35" stop-color="#c98f74"/>
        <stop offset="0.65" stop-color="#5a78b8"/>
        <stop offset="1" stop-color="#d9d6d3"/>
      </linearGradient>
    </defs>
    <use href="#wave-edge" transform="translate(-48 48)" fill="var(--brand-sky)"/>
    <use href="#wave-edge" transform="translate(-24 24)" fill="var(--band-deep)"/>
    <use href="#wave-edge" fill="url(#photo-tone)" role="img" aria-label="Photo of a technician in a hard hat and blue overalls repairing water pipes against a brick wall"/>
  </svg>
</main>
</body>
</html>
```